Bauzaunplane für Weihnachtsmarkt
Zielgruppe
Endverbraucher, die den Weihnachtsmarkt besuchen / besuchen sollen.
Aufgabenstellung
Benötigt wird ein Entwurf für eine Bauzaunplane (B) 2,12m x (H) 1,72m. Diese wird auf einem Weihnachtsmarkt als Sichtblende eingesetzt.
Die Gestaltung soll Atmosphäre vermitteln und ggf. Bezug zu Nikolaus, Engeln und anderen Adventssysmbolen nehmen (Hinweis: Der Weihnachtsmann kommt ind er Bibel nicht vor!)
Der Claim" Wir wünschen Ihnen eine schöne Zeit auf dem Quendlitzer Weihnachtsmarkt" soll in das Motiv integriert werden.
Das Banner wird anschließend im Digitaldruck 4/0 C produziert. gefordert ist abschließend eine druckfähige Vorlage mit ausreichender Auflösung (ca. 100dpi auf das Endformat) vorzugsweise PDF/X3 - ISOcoatedV2ECI.

```html
<!DOCTYPE html>
<html lang="de">
<head>
<meta charset="utf-8">
<title>Quendlitzer Weihnachtsmarkt – Bauzaunplane</title>
<link rel="stylesheet" href="https://fonts.googleapis.com/css2?family=Rye&family=Pinyon+Script&display=swap">
<style>
  :root {
    --gold-light: #fbe9b8;
    --gold-mid: #f0c04a;
    --gold-deep: #d8901c;
    --amber-edge: #c97f17;
    --festive-red: #b8141f;
    --ornament-red: #8e1418;
    --ornament-bright: #c8202a;
    --ornament-gold: #d9a22a;
  }
  * { margin: 0; padding: 0; box-sizing: border-box; }
  html, body {
    width: 1200px;
    height: 974px;
    overflow: hidden;
  }
  .banner {
    position: relative;
    width: 1200px;
    height: 974px;
    overflow: hidden;
    background:
      radial-gradient(ellipse 620px 520px at 600px 640px,
        var(--gold-light) 0%, var(--gold-mid) 55%, var(--gold-deep) 85%, var(--amber-edge) 100%);
  }
  .ornament-garland {
    position: absolute;
    left: 0;
    top: 0;
    width: 1200px;
    height: 540px;
    border-radius: 0 0 48% 48% / 0 0 30% 30%;
    background: linear-gradient(90deg,
      var(--ornament-bright) 0%,
      var(--ornament-red) 14%,
      var(--ornament-gold) 26%,
      var(--ornament-red) 44%,
      var(--ornament-gold) 60%,
      var(--ornament-bright) 74%,
      var(--ornament-gold) 88%,
      var(--ornament-bright) 100%);
    -webkit-mask-image: linear-gradient(180deg, #000 0%, #000 62%, rgba(0,0,0,0.35) 88%, transparent 100%);
    mask-image: linear-gradient(180deg, #000 0%, #000 62%, rgba(0,0,0,0.35) 88%, transparent 100%);
  }
  .claim {
    position: absolute;
    left: 0;
    width: 1200px;
    text-align: center;
    color: var(--festive-red);
    white-space: nowrap;
  }
  .claim-intro {
    top: 556px;
    font-family: "Pinyon Script", cursive;
    font-size: 66px;
    line-height: 1;
  }
  .market-name {
    top: 668px;
    font-family: "Rye", serif;
    font-size: 100px;
    line-height: 1;
    letter-spacing: 1px;
    transform: scaleY(1.3);
    transform-origin: 50% 0;
  }
  .market-type {
    top: 812px;
    font-family: "Rye", serif;
    font-size: 76px;
    line-height: 1;
    letter-spacing: 8px;
  }
  .market-type .initial {
    font-size: 100px;
  }
</style>
</head>
<body>
  <main class="banner">
    <div class="ornament-garland" role="img" aria-label="Girlande aus roten und goldenen Christbaumkugeln, Sternen, Glocken mit Schleife, Perlenketten und Zuckerstangen"></div>
    <p class="claim claim-intro">Wir wünschen Ihnen eine schöne Zeit auf dem</p>
    <h1 class="claim market-name">QUENDLITZER</h1>
    <p class="claim market-type"><span class="initial">W</span>EIHNACHTSMARKT</p>
  </main>
</body>
</html>
```